Non-Profit Organization Needs WordPress websiteTo Empower Women

Our client is a Non-profit organization that requires a responsively-designed WordPress website to help publish their online magazine. This website will also feature their magazine publication that they publish quarterly. The design will need to be mobile-friendly, so it looks great on all devices.

The main purpose of this site is the following, in order of importance:
1. Educate economically-challenged women to improve their lives with blog content and their online Magazine.
2. Create a Membership community for these women to help one another. THE MAIN CALL-TO-ACTION ON THE SITE IS TO MOTIVATE THE READERS TO JOIN THE FREE MEMBERSHIP COMMUNITY.
3. Recognize and Identify the contributing Organizations, and to motivate the organizations to donate money to the non-profit organization.

Here is information from the client about what they want for their website:
*********************************************************************************************
It needs to have two entrances to content: Organizations & Readers; Don't like cluttered which some magazine formats seem to be. Like edgy, yet feminine. Not sweet. Easy to navigate and find what one comes to find. Colorful.

We need: A Resources area, a Donation button prominently placed on the site, section for archived magazine articles; Place for translated issues. We will want to have a private Membership section on the site. (NOTE: These requests should be used to help create the site's navigation menu.)

Here are example websites the client likes and why. Please use them as inspiration.
http:://www.brindlewave.com color, simple design w cool buttons, uncluttered
http:://www.tolvarick.com emotion with the color, ease of getting around
http:://www.quenderpast7.com the second page has the color sections that take you to next page
http:://www.marrowlightjournal.com not sweetly feminine, perhaps community style
http:://www.pellicrest.net use of clear symbols, newer design/graphics look

Target Market(s)

The website targets 2 different audiences: Organizations that help to provide services and help to the website readers, and the Readers themselves. The Readers are mostly economically-challenged females that need inspiration and help. The Readers should be considered the Primary Target Audience, with the Organizations being secondary.

Industry/Entity Type

Non-Profit

Font styles to use
Sans Serif

Colors
f37022
fece3e

Requirements
Must have
• The final design MUST, MUST, MUST be created using Separate PSD layers for each element and graphic! PLEASE create a professional layer structure within your design, so we can code it properly.

Please do NOT use Graphics/Images where Text should be used. Examples of this are the business address, phone number, etc.

The website home page design should identify its two main audiences, the Organizations and the Readers. The main call to action is to invite the Readers to become free members of their membership community.

There MUST be an area on the home page where their online magazine can be embedded onto their site OR an image button etc that leads to the magazine. They use the http://vondrel.com/ system to create the magazine and then embed the issues on their site. Alternatively, you could create a button, image, area, etc, where the user can click the image and then go to the magazine.

A membership login field OR a button that leads to a Members login area.

A small area on the website that either Adsense or advertising can be used, and this MUST be BELOW the FOLD.

The site must project a sense of hope and/or empowerment for its Readers. The imagery should resonate with females who want to be inspired.
Nice to have
• There should be links or buttons to identify Spanish-speaking Readers and Portuguese-speaking Readers.
Should not have
• NO Gallery Sliders or Photo Sliders

```html
<!DOCTYPE html>
<html lang="en">
<head>
<meta charset="utf-8">
<title>RiseWell</title>
<link href="https://fonts.googleapis.com/css2?family=Arimo:wght@400;700&family=Open+Sans:wght@300;400;600;700&family=Signika:wght@600;700&display=swap" rel="stylesheet">
<style>
:root{
  --orange:#f26a30;
  --orange-deep:#e8521e;
  --red:#d9381e;
  --yellow:#fece3e;
  --gold:#f6c342;
  --ink:#333;
  --muted:#9a9a9a;
  --blue:#1f6fb2;
  --line:#e4e0dc;
  --peach:#fdf1ea;
  --navy:#1d2733;
  --navy-deep:#151d27;
  --gray-band:#d8cfc8;
}
*{box-sizing:border-box;margin:0;padding:0}
html,body{width:751px;height:1200px;overflow:hidden}
body{position:relative;background:#fff;font-family:"Arimo",Arial,sans-serif;color:var(--ink)}
.abs{position:absolute}
.page-bg{left:62px;top:0;width:626px;height:1200px;background:#fff;border-left:1px solid var(--line);border-right:1px solid var(--line)}
.side-tint{left:688px;top:46px;width:36px;height:1154px;background:var(--peach)}
.top-bar{left:62px;top:0;width:626px;height:33px;background:var(--orange)}
.top-stripe{left:62px;top:33px;width:626px;height:5px;background:var(--yellow)}
.top-links{left:78px;top:12px;font:700 7.5px "Open Sans",sans-serif;color:#fff;letter-spacing:.2px}
.top-links span{margin-right:10px}
.call{left:486px;top:9px;font:400 12px "Open Sans",sans-serif;color:#fff}
.brand{left:70px;top:50px;display:flex;align-items:center;gap:6px;font:700 30px "Open Sans",sans-serif;color:var(--orange)}
.brand i{width:14px;height:14px;background:var(--yellow);display:block}
.search{left:422px;top:60px;width:245px;height:23px;border:1px solid #ddd;border-radius:2px;font:400 8px "Open Sans",sans-serif;color:#888;padding:6px 6px}
.search svg{position:absolute;right:6px;top:5px}
.nav{left:62px;top:98px;width:626px;height:35px;background:var(--orange);border-radius:0 0 4px 4px}
.nav-item{top:112px;font:700 8.5px "Open Sans",sans-serif;color:#fff}
.nav-home{left:78px;top:104px;width:45px;height:24px;background:var(--yellow);border-radius:2px;font:700 8.5px "Open Sans",sans-serif;color:#fff;padding:8px 0 0 8px}
.nav-donate{left:598px;top:104px;width:70px;height:24px;background:var(--yellow);border-radius:2px;font:700 8.5px "Open Sans",sans-serif;color:var(--orange-deep);text-align:center;padding-top:8px}
.hero{left:77px;top:145px;width:591px;height:232px;border:1px solid #ccc;background:linear-gradient(90deg,#e9e4de,#d5d1cc 40%,#ece9e6)}
.hero-photo{left:78px;top:146px;width:210px;height:230px;background:linear-gradient(180deg,#efe7de,#c9b9a6)}
.hero-band{left:78px;top:310px;width:589px;height:47px;background:rgba(255,255,255,.45)}
.hero-card{left:382px;top:195px;width:281px;height:112px;background:var(--gold);padding:14px 20px}
.hero-card h2{font:700 10.5px "Open Sans",sans-serif;color:#fff;letter-spacing:.3px}
.hero-card p{font:400 7.3px/11px "Open Sans",sans-serif;color:#fff;margin-top:4px}
.join{left:403px;top:268px;width:100px;height:29px;background:var(--orange-deep);border:2px solid #fff;border-radius:3px;font:600 10.5px "Open Sans",sans-serif;color:#fff;text-align:center;padding-top:6px}
.hero-head{left:238px;top:320px;font:700 17.5px "Signika",sans-serif;color:var(--orange);letter-spacing:1px}
.tab{height:20px;font:700 9.5px "Arimo",sans-serif;color:#fff;padding:5px 0 0 14px}
.tab.orange{background:var(--orange-deep);transform:skewX(-8deg)}
.tab span{display:block;transform:skewX(8deg)}
.rule{height:3px;background:var(--orange-deep)}
.biz-photo{left:78px;top:425px;width:298px;height:162px;background:linear-gradient(135deg,#c8cdd2,#8d969e 55%,#e2e4e6)}
.biz-cap{left:78px;top:587px;width:298px;height:50px;background:var(--gray-band);padding:10px 13px;font:400 8.5px "Arimo",sans-serif}
.biz-cap .cat{color:var(--blue)}
.stars{color:var(--red);font-size:8px;letter-spacing:1px}
.biz-box{left:78px;top:642px;width:297px;height:90px;background:var(--orange-deep);padding:9px 11px;font:400 8.3px/11.5px "Arimo",sans-serif;color:#fff}
.biz-box .meta{margin-top:10px}
.social{top:423px;width:19px;height:19px;border-radius:2px}
.sb-thumb{left:398px;width:98px;height:57px}
.sb-title{left:500px;font:400 12.5px "Open Sans",sans-serif;color:#333}
.sb-meta{left:500px;font:400 5.5px "Open Sans",sans-serif;color:#aaa}
.sb-text{left:500px;font:400 7.8px/12px "Open Sans",sans-serif;color:#444;width:170px}
.sb-sep{left:398px;width:270px;height:1px;background:var(--line)}
.pop-panel{left:78px;top:750px;width:590px;height:208px;background:#fff;box-shadow:0 0 4px rgba(0,0,0,.25)}
.dark-tab{left:83px;top:760px;width:124px;height:21px;background:#2a2a2a;font:700 9.5px "Arimo",sans-serif;color:#fff;padding:5px 0 0 10px}
.dark-rule{left:83px;top:779px;width:576px;height:3px;background:#2a2a2a}
.card{top:792px;width:137px;height:161px;background:#fff;border:1px solid #eee}
.card .img{height:87px}
.card h3{font:400 7.4px/11px "Arimo",sans-serif;color:#111;padding:9px 12px 0;height:41px}
.card .tags{font:400 6px "Arimo",sans-serif;color:#999;padding:3px 12px 0;height:20px}
.card .foot{background:var(--red);height:26px;color:#fff;font:400 7.4px "Arimo",sans-serif;padding:9px 5px;display:flex;gap:23px}
.footer{left:78px;top:978px;width:590px;height:222px;background:var(--navy)}
.footer-base{left:78px;top:1176px;width:590px;height:24px;background:var(--navy-deep);font:400 7.5px "Arimo",sans-serif;color:#bbb;text-align:center;padding-top:8px}
.f-head{top:985px;font:700 10px "Arimo",sans-serif;color:#fff}
.f-rule{top:1000px;height:1px;background:#33404f}
.f-brand{left:103px;top:1003px;font:700 28px "Open Sans",sans-serif;color:#4a5664}
.f-text{left:99px;font:400 6.6px/12.5px "Open Sans",sans-serif;color:#ccd}
.f-input{left:99px;top:1110px;width:117px;height:18px;background:#273341;font:400 6.5px "Open Sans",sans-serif;color:#aab;padding:5px 7px}
.f-btn{left:219px;top:1110px;width:41px;height:18px;background:#34445a;font:400 6.5px "Open Sans",sans-serif;color:#fff;text-align:center;padding-top:5px}
.t-thumb{left:295px;width:39px;height:33px}
.t-date{left:345px;font:400 5.3px "Open Sans",sans-serif;color:#aab}
.t-title{left:345px;font:400 7px/10.5px Georgia,serif;color:#fff;width:125px}
.t-count{left:453px;font:400 5.3px "Open Sans",sans-serif;color:#aab}
.t-sep{left:295px;width:171px;height:1px;background:#2f3b49}
.snap{width:35px;height:31px}
</style>
</head>
<body>
<div class="abs page-bg"></div>
<div class="abs side-tint"></div>

<header>
  <div class="abs top-bar"></div>
  <div class="abs top-stripe"></div>
  <div class="abs top-links"><span>READERS</span><span>ORGANIZATIONS</span><span>ESPAÑOL</span><span>PORTUGUÊS</span></div>
  <div class="abs call">CALL US : (555)-240-318</div>
  <div class="abs brand"><i></i>RiseWell</div>
  <div class="abs search">search tab
    <svg width="12" height="12" viewBox="0 0 12 12"><circle cx="5" cy="5" r="4" fill="none" stroke="#1f4a7a" stroke-width="1.6"/><line x1="8" y1="8" x2="11" y2="11" stroke="#1f4a7a" stroke-width="1.8"/></svg>
  </div>
  <nav>
    <div class="abs nav"></div>
    <div class="abs nav-home">HOME</div>
    <div class="abs nav-item" style="left:141px">MAGAZINE</div>
    <div class="abs nav-item" style="left:202px">RESOURCES</div>
    <div class="abs nav-item" style="left:268px">ARCHIVES</div>
    <div class="abs nav-item" style="left:327px">TRANSLATED ISSUES</div>
    <div class="abs nav-item" style="left:428px">MEMBERS LOGIN</div>
    <div class="abs nav-donate">DONATE</div>
  </nav>
</header>

<section class="feature">
  <div class="abs hero"></div>
  <div class="abs hero-photo" role="img" aria-label="Smiling woman in a light blazer giving a thumbs up"></div>
  <div class="abs hero-band"></div>
  <div class="abs hero-card">
    <h2>join our free membership community</h2>
    <p>Women helping women: share stories, find resources and read every quarterly issue of our magazine. Membership is free and open to all readers....</p>
  </div>
  <div class="abs join">JOIN FREE</div>
  <div class="abs hero-head">LEARN. GROW. RISE TOGETHER.</div>
</section>

<section class="readers">
  <div class="abs tab orange" style="left:82px;top:394px;width:96px"><span>FOR READERS</span></div>
  <div class="abs rule" style="left:80px;top:412px;width:296px"></div>
  <div class="abs biz-photo" role="img" aria-label="Grey-haired businessman talking on a mobile phone"></div>
  <div class="abs biz-cap">
    <div class="cat">✎ MAGAZINE</div>
    <div>Read the latest quarterly issue online</div>
    <div class="stars">★★★★<span style="color:#bbb">★</span></div>
  </div>
  <div class="abs biz-box">
    simply dummy text of the printing and typesetting industry. Lorem Ipsum has been the industry's standard dummy text ever since the 1500s, when an unknown printer took a galley of type and scrambled it to make a type specimen book.
    <div class="meta">&#9679; mlarent &nbsp;&nbsp;&nbsp; &#9635; January 29, 2014</div>
  </div>
</section>

<aside class="sidebar">
  <div class="abs tab orange" style="left:406px;top:392px;width:64px"><span>FOLLOW</span></div>
  <div class="abs rule" style="left:404px;top:410px;width:264px"></div>
  <div class="abs social" style="left:403px;background:#f8b449"></div>
  <div class="abs social" style="left:426px;background:#e4493b"></div>
  <div class="abs social" style="left:448px;background:#3d5f9a"></div>
  <div class="abs social" style="left:471px;background:#4ab3e6"></div>
  <div class="abs social" style="left:494px;background:#e0444d"></div>
  <div class="abs social" style="left:516px;background:#ec8bb0"></div>
  <div class="abs social" style="left:539px;background:#c8302b"></div>
  <div class="abs social" style="left:561px;background:#6c8fb4"></div>

  <div class="abs tab orange" style="left:404px;top:468px;width:64px"><span>POPULAR</span></div>
  <div class="abs tab" style="left:472px;top:468px;width:64px;background:var(--gold);transform:skewX(-8deg)"><span style="transform:skewX(8deg);display:block">RECENT</span></div>
  <div class="abs rule" style="left:402px;top:487px;width:266px"></div>

  <div class="abs sb-thumb" style="top:505px;background:linear-gradient(135deg,#dfe6ec,#b9c6d2)" role="img" aria-label="Scientists in lab coats"></div>
  <div class="abs sb-title" style="top:504px">Post With Featured Image</div>
  <div class="abs sb-meta" style="top:526px">◷ July 30, 2012 &nbsp; 35 Comments &nbsp; 22,118 Views</div>
  <div class="abs sb-text" style="top:535px">Diam 1989 wisi quam lorem vestibulum nec sollicitudin volutpat at libero ...</div>
  <div class="abs sb-sep" style="top:568px"></div>

  <div class="abs sb-thumb" style="top:585px;background:linear-gradient(135deg,#7fb2da,#e9eef2)" role="img" aria-label="Woman in a white sun hat"></div>
  <div class="abs sb-title" style="top:584px;left:502px">Post With Featured Image</div>
  <div class="abs sb-meta" style="top:606px;left:502px">◷ July 30, 2012 &nbsp; 35 Comments &nbsp; 22,118 Views</div>
  <div class="abs sb-text" style="top:615px;left:502px">Diam 1989 wisi quam lorem vestibulum nec sollicitudin volutpat at libero ...</div>
  <div class="abs sb-sep" style="top:648px"></div>

  <div class="abs sb-thumb" style="top:661px;left:397px;background:linear-gradient(135deg,#2a2320,#8a4a2a)" role="img" aria-label="Guitarist playing an electric guitar"></div>
  <div class="abs sb-title" style="top:667px;left:502px">Post With Featured Image</div>
  <div class="abs sb-meta" style="top:689px;left:502px">◷ July 30, 2012 &nbsp; 35 Comments &nbsp; 22,118 Views</div>
  <div class="abs sb-text" style="top:698px;left:502px">Diam 1989 wisi quam lorem vestibulum nec sollicitudin volutpat at libero ...</div>
  <div class="abs sb-sep" style="top:731px"></div>
</aside>

<section class="organizations">
  <div class="abs pop-panel"></div>
  <div class="abs dark-tab">FOR ORGANIZATIONS</div>
  <div class="abs dark-rule"></div>
  <div class="abs card" style="left:82px">
    <div class="img" style="background:linear-gradient(160deg,#5a6f8a,#c9b23a)" role="img" aria-label="Woman in a yellow dress among feathers"></div>
    <h3>Lorem ipsum dolor sit amet vel nisi amet ve</h3>
    <div class="tags">Education &amp; DIY, Everyday Life</div>
    <div class="foot"><span>1944 Views</span><span>Feb 02, 2014</span></div>
  </div>
  <div class="abs card" style="left:231px">
    <div class="img" style="background:linear-gradient(160deg,#3a3632,#c7ad8e)" role="img" aria-label="Woman with curly blonde hair"></div>
    <h3>Lorem ipsum dolor sit amet vel nisi amet ve</h3>
    <div class="tags">Video School, Web Series</div>
    <div class="foot"><span>1944 Views</span><span>Feb 02, 2014</span></div>
  </div>
  <div class="abs card" style="left:381px">
    <div class="img" style="background:linear-gradient(160deg,#f2f2f2,#3a3a3a)" role="img" aria-label="Young man in a black leather jacket"></div>
    <h3>Lorem ipsum dolor sit amet vel nisi amet ve</h3>
    <div class="tags">Motion Graphics, Projects</div>
    <div class="foot"><span>1944 Views</span><span>Feb 02, 2014</span></div>
  </div>
  <div class="abs card" style="left:527px">
    <div class="img" style="background:linear-gradient(160deg,#c8ccd0,#6b5a4e)" role="img" aria-label="Dark-haired man portrait"></div>
    <h3>Lorem ipsum dolor sit amet vel nisi amet ve</h3>
    <div class="tags">Best Clips, Comedy</div>
    <div class="foot"><span>1944 Views</span><span>Feb 02, 2014</span></div>
  </div>
</section>

<footer>
  <div class="abs footer"></div>
  <div class="abs f-head" style="left:99px">ABOUT</div>
  <div class="abs f-head" style="left:295px">TECHNOLOGY</div>
  <div class="abs f-head" style="left:490px">SNAPSHOTS</div>
  <div class="abs f-rule" style="left:99px;width:172px"></div>
  <div class="abs f-rule" style="left:295px;width:171px"></div>
  <div class="abs f-rule" style="left:490px;width:160px"></div>
  <div class="abs f-brand">RiseWell</div>
  <div class="abs f-text" style="top:1041px;width:170px">Neque porro quisquam est qui dolorem ipsum quia dolor sit amet, consectetur. Lorem Ipsum is simply dummy text of the printing and typesetting industry.</div>
  <div class="abs f-text" style="top:1090px">Subscribe to our newsletter:</div>
  <div class="abs f-input">Email Address</div>
  <div class="abs f-btn">SUBMIT</div>

  <div class="abs t-thumb" style="top:1011px;background:linear-gradient(135deg,#5e7a48,#c9c3b6)" role="img" aria-label="Green robot toy"></div>
  <div class="abs t-date" style="top:1016px">DEC 16, 2013</div>
  <div class="abs t-count" style="top:1016px">❑ 4</div>
  <div class="abs t-title" style="top:1026px">Robot Toy Restyled Again for the Latest Phone</div>
  <div class="abs t-sep" style="top:1051px"></div>

  <div class="abs t-thumb" style="top:1064px;background:linear-gradient(135deg,#5fb4c4,#2a2a2a)" role="img" aria-label="Fashion model"></div>
  <div class="abs t-date" style="top:1065px">DEC 16, 2013</div>
  <div class="abs t-count" style="top:1065px">❑ 1</div>
  <div class="abs t-title" style="top:1075px">Fashion Trends Updates for the Upcoming Summer</div>
  <div class="abs t-sep" style="top:1101px"></div>

  <div class="abs t-thumb" style="top:1113px;background:linear-gradient(135deg,#8a7a6a,#e2d6c4)" role="img" aria-label="Gold rings"></div>
  <div class="abs t-date" style="top:1114px">DEC 16, 2013</div>
  <div class="abs t-count" style="top:1114px">❑ 1</div>
  <div class="abs t-title" style="top:1124px">My Precious, the Ring Saga 4th Espiode Arrived</div>
  <div class="abs t-sep" style="top:1150px"></div>

  <div class="abs snap" style="left:490px;top:1012px;background:#5a4a44" role="img" aria-label="Gallery photo"></div>
  <div class="abs snap" style="left:531px;top:1012px;background:#8e9aa0" role="img" aria-label="Gallery photo"></div>
  <div class="abs snap" style="left:571px;top:1012px;background:#c9a8b8" role="img" aria-label="Gallery photo"></div>
  <div class="abs snap" style="left:612px;top:1012px;background:#9a7a5a" role="img" aria-label="Gallery photo"></div>
  <div class="abs snap" style="left:490px;top:1051px;background:#4a3a9a" role="img" aria-label="Gallery photo"></div>
  <div class="abs snap" style="left:531px;top:1051px;background:#c8a070" role="img" aria-label="Gallery photo"></div>
  <div class="abs snap" style="left:571px;top:1051px;background:#3a4a6a" role="img" aria-label="Gallery photo"></div>
  <div class="abs snap" style="left:612px;top:1051px;background:#7a7a74" role="img" aria-label="Gallery photo"></div>
  <div class="abs snap" style="left:490px;top:1089px;background:#3a5a8a" role="img" aria-label="Gallery photo"></div>
  <div class="abs snap" style="left:531px;top:1089px;background:#b07a5a" role="img" aria-label="Gallery photo"></div>
  <div class="abs snap" style="left:571px;top:1089px;background:#8aa0c0" role="img" aria-label="Gallery photo"></div>
  <div class="abs snap" style="left:612px;top:1089px;background:#2a2a6a" role="img" aria-label="Gallery photo"></div>

  <div class="abs footer-base">Copyright (C) 2014 - RiseWell . All rights reserved.</div>
</footer>
</body>
</html>
```